'TOLVANTA' NEW WINE LABEL DESIGN

I am looking for an exceptional and exciting design for a wine label called 'Tolvanta' meaning 'Lookout'. The design must feature the name 'Tolvanta', and the word 'Cabernet Sauvignon' in version 1 and 'Sauvignon Blanc' in version 2. It will also need the words 'Valle Central, Chile' at the bottom of the label as a prominent piece of information as well as the vintage 2017. Please produce the work in size 80mm x 100mm. Feel free to use colour in addition to black/white and ensue that the label is easy to read on a shelf placement.
Target Market(s)
SUPERMARKETS & WINE STORES
Requirements
Must have
- EASY TO READ, USE COLOURS LIKE GREEN FOR SAUVIGNON & RED FOR CABERNET SAUVIGNON
- FULL BOTTLE SHOT MUST BE IN PROVIDED DESIGNS. ALL BOTTLE TOPS SHOULD BE QUORLAN STYLE (SCREW TOP)
- PLEASE NOTE THAT LABEL INFORMATION MUSY BE EASY TO READ I.E. VINTAGE, PLACE OF ORGIN ALTHOUGH NOT THE MAIN CONTENT MUST STILL BE CLEAR.
Nice to have
- ARTISTIC REFERENCE LINK TO NAME & ANDES BUT NOT PICTURES OF MOUNTAINS
Should not have
- PICTURES OF GRAPES
- PICTURES OF VINEYARDS
- PICTURES OF MOUNTAINS

```html
<!DOCTYPE html>
<html lang="en">
<head>
<meta charset="utf-8">
<title>Tolvanta – Cabernet Sauvignon Label</title>
<link rel="stylesheet" href="https://fonts.googleapis.com/css2?family=Cinzel:wght@400;500&family=Cormorant+SC:wght@500;600&family=Pinyon+Script&family=Montserrat:wght@500&display=swap">
<style>
  :root {
    --page-bg: #ffffff;
    --label-paper: #ebe9e7;
    --ink-dark: #1f1d1f;
    --ink-gold: #7d6a45;
    --ink-script: #2b2a2a;
    --ink-year: #5b4b31;
    --rule: #b9b2a4;
    --wash-rose: #d9788f;
    --wash-berry: #a9416a;
    --wash-violet: #6f5f9c;
    --wash-gold: #d8c25a;
  }
  * { margin: 0; padding: 0; box-sizing: border-box; }
  html, body {
    width: 1200px;
    height: 1200px;
    overflow: hidden;
    background: var(--page-bg);
  }
  .canvas {
    position: relative;
    width: 1200px;
    height: 1200px;
    display: flex;
    align-items: center;
    justify-content: center;
  }
  .wine-label {
    position: relative;
    width: 800px;
    height: 1000px;
    background: var(--label-paper);
    box-shadow: 0 2px 14px rgba(0,0,0,0.08);
  }
  .label-artwork {
    position: absolute;
    top: 170px;
    left: 230px;
    width: 500px;
    height: 190px;
    border-radius: 50% 40% 45% 55% / 60% 50% 50% 40%;
    background: linear-gradient(100deg,
      rgba(217,120,143,0.15) 0%,
      var(--wash-rose) 22%,
      var(--wash-berry) 42%,
      var(--wash-violet) 62%,
      var(--wash-gold) 80%,
      rgba(216,194,90,0.25) 100%);
    opacity: 0.85;
  }
  .brand-name {
    position: absolute;
    top: 440px;
    left: 0;
    width: 100%;
    text-align: center;
    font-family: "Cinzel", serif;
    font-weight: 400;
    font-size: 70px;
    letter-spacing: 4px;
    color: var(--ink-dark);
    line-height: 1;
  }
  .divider {
    position: absolute;
    top: 548px;
    left: 350px;
    width: 100px;
    height: 1px;
    background: var(--rule);
  }
  .varietal {
    position: absolute;
    top: 580px;
    left: 0;
    width: 100%;
    text-align: center;
    font-family: "Cormorant SC", serif;
    font-weight: 600;
    font-size: 28px;
    letter-spacing: 3px;
    color: var(--ink-gold);
  }
  .origin {
    position: absolute;
    top: 620px;
    left: 0;
    width: 100%;
    text-align: center;
    font-family: "Pinyon Script", cursive;
    font-size: 42px;
    color: var(--ink-script);
  }
  .vintage {
    position: absolute;
    top: 688px;
    left: 0;
    width: 100%;
    text-align: center;
    font-family: "Montserrat", sans-serif;
    font-weight: 500;
    font-size: 22px;
    letter-spacing: 4px;
    color: var(--ink-year);
  }
</style>
</head>
<body>
  <main class="canvas">
    <section class="wine-label">
      <div class="label-artwork" role="img" aria-label="Loose watercolour wash in rose, berry, violet and gold tones evoking a lookout view"></div>
      <h1 class="brand-name">TOLVANTA</h1>
      <div class="divider"></div>
      <p class="varietal">Cabernet Sauvignon</p>
      <p class="origin">Valle Central, Chile</p>
      <p class="vintage">2017</p>
    </section>
  </main>
</body>
</html>
```